Virtual assistant company needs letterhead and email signature

We need a letterhead and email signature for our virtual assistant company - taskBeaver (small w capital F). Our tag line is plan ahead | taskBeaver

The colours we would like used are;

#81788c
#dddbe1

For reference our business cards have used #81788c background colour and #dddbe1 text

The fonts we would like used are

Lora
Proxima Nova

Please check out our twitter and facebook for style and feel

Twitter: @taskbeaver
www.examplebook.test/taskbeaver

Please also find attached our landing page and business cards for reference

Any questions please let us know

Thanks
E

Reason: We like the opportunity to receive furthur designs

```html
<!DOCTYPE html>
<html lang="en">
<head>
<meta charset="utf-8">
<title>taskBeaver email signature</title>
<link rel="stylesheet" href="https://fonts.googleapis.com/css2?family=Montserrat:wght@400&display=swap">
<style>
  :root {
    --brand-plum: #81788c;
    --brand-mist: #dddbe1;
    --ink: #2f2f33;
    --page: #ffffff;
  }
  * { margin: 0; padding: 0; box-sizing: border-box; }
  html, body {
    width: 1200px;
    height: 1000px;
    overflow: hidden;
    background: var(--page);
  }
  .signature {
    position: absolute;
    left: 330px;
    top: 330px;
    width: 540px;
  }
  .brand-plate {
    width: 500px;
    height: 138px;
    background: var(--brand-plum);
    color: var(--brand-mist);
    font-family: "Montserrat", sans-serif;
    font-weight: 400;
    display: flex;
    flex-direction: column;
    justify-content: center;
    padding-left: 32px;
  }
  .brand-name {
    font-size: 46px;
    line-height: 1.1;
  }
  .brand-tagline {
    font-size: 20px;
    margin-top: 10px;
  }
  .contact-block {
    position: relative;
    margin-left: 25px;
    padding-top: 28px;
    padding-bottom: 30px;
  }
  .contact-rail {
    position: absolute;
    left: 0;
    top: 0;
    bottom: 0;
    width: 40px;
    background: var(--brand-mist);
  }
  .contact-line {
    position: relative;
    display: flex;
    align-items: center;
    height: 44px;
  }
  .contact-icon {
    width: 40px;
    display: flex;
    justify-content: center;
  }
  .contact-icon svg { width: 24px; height: 24px; fill: var(--brand-plum); }
  .contact-text {
    font-family: "Montserrat", sans-serif;
    font-weight: 400;
    font-size: 33px;
    color: var(--ink);
    padding-left: 8px;
    white-space: nowrap;
  }
</style>
</head>
<body>
  <div class="signature">
    <div class="brand-plate">
      <div class="brand-name">taskBeaver</div>
      <div class="brand-tagline">plan ahead | taskBeaver</div>
    </div>
    <div class="contact-block">
      <div class="contact-rail"></div>
      <div class="contact-line">
        <span class="contact-icon">
          <svg viewBox="0 0 24 24" aria-hidden="true"><path d="M6.6 10.8c1.4 2.8 3.8 5.1 6.6 6.6l2.2-2.2c.3-.3.7-.4 1-.2 1.1.4 2.3.6 3.6.6.6 0 1 .4 1 1V20c0 .6-.4 1-1 1C10.6 21 3 13.4 3 4c0-.6.4-1 1-1h3.5c.6 0 1 .4 1 1 0 1.3.2 2.5.6 3.6.1.3 0 .7-.2 1z"/></svg>
        </span>
        <span class="contact-text">+ 55 11 3000 0199</span>
      </div>
      <div class="contact-line">
        <span class="contact-icon">
          <svg viewBox="0 0 24 24" aria-hidden="true"><path d="M2 6h20v2l-10 6L2 8z"/><path d="M2 10l10 6 10-6v8H2z"/></svg>
        </span>
        <span class="contact-text">info@taskbeaver.test</span>
      </div>
      <div class="contact-line">
        <span class="contact-icon">
          <svg viewBox="0 0 24 24" aria-hidden="true"><circle cx="12" cy="12" r="9"/></svg>
        </span>
        <span class="contact-text">www.taskbeaver.test</span>
      </div>
    </div>
  </div>
</body>
</html>
```